Fernvale Stationary
I need single sided standard sized Business Card [3.5" x 2"]
Prefer same font as logo, however would like to see how it looks with a different font
Simple
Suresh Kodandaraman
CEO
No. 17, 60 ft Road,
Fourth block, Hesaralu
Bengalooru 560071
Karnataka
INDIA
suresh.kodand@fernvaledental.example

```html
<!DOCTYPE html>
<html lang="en">
<head>
<meta charset="utf-8">
<title>Fernvale Dental Stationery</title>
<link rel="stylesheet" href="https://fonts.googleapis.com/css2?family=Cinzel:wght@500&family=Open+Sans:wght@400;600&display=swap">
<style>
  :root {
    --backdrop: #2e2c2d;
    --paper: #ffffff;
    --plum: #5a2b56;
    --plum-soft: #6d3a68;
    --silver: #c9c9cb;
    --ink: #4a4a4a;
    --ink-light: #7a7a7a;
  }
  * { margin: 0; padding: 0; box-sizing: border-box; }
  html, body { width: 1200px; height: 718px; overflow: hidden; }
  body {
    background: var(--backdrop);
    position: relative;
    font-family: "Open Sans", Arial, sans-serif;
    color: var(--ink);
  }
  .sheet { position: absolute; background: var(--paper); overflow: hidden; }
  .brand {
    font-family: "Cinzel", Georgia, serif;
    font-weight: 500;
    color: var(--plum);
    letter-spacing: 0.06em;
    white-space: nowrap;
    display: flex;
    align-items: center;
    gap: 6px;
  }
  .brand-dot { border-radius: 50%; background: currentColor; flex: none; }
  .brand-on-plum { color: var(--paper); }
  .band { position: absolute; left: 0; bottom: 0; width: 100%; }
  .small-text { font-size: 5.5px; line-height: 1.5; color: var(--ink-light); font-style: normal; }

  /* business card front */
  .card-front { left: 62px; top: 72px; width: 178px; height: 92px; }
  .card-front .person { position: absolute; left: 12px; top: 38px; font-size: 6.5px; font-weight: 600; color: var(--ink); white-space: nowrap; }
  .card-front .person span { display: block; font-weight: 400; font-size: 5.5px; color: var(--ink-light); }
  .card-front .contact { position: absolute; left: 100px; top: 24px; width: 70px; white-space: nowrap; }

  /* business card back, white */
  .card-back { left: 259px; top: 72px; width: 178px; height: 92px; display: flex; align-items: center; justify-content: center; }
  .card-back .brand { font-size: 10px; }

  /* business card back, plum */
  .card-plum { left: 456px; top: 72px; width: 178px; height: 92px; background: var(--plum); display: flex; align-items: center; justify-content: center; }
  .card-plum .brand { font-size: 10px; }

  /* envelope back */
  .envelope-back { left: 101px; top: 211px; width: 456px; height: 221px; }
  .envelope-back .flap { position: absolute; left: 0; top: 0; width: 100%; height: 130px; }
  .envelope-back .brand { position: absolute; left: 50%; top: 28px; transform: translateX(-50%); font-size: 12px; }
  .envelope-back .return { position: absolute; left: 22px; top: 150px; }

  /* envelope front */
  .envelope-front { left: 101px; top: 461px; width: 456px; height: 211px; }
  .envelope-front .brand { position: absolute; left: 28px; top: 40px; font-size: 14px; }
  .envelope-front .return { position: absolute; left: 28px; top: 70px; }

  /* letterhead */
  .letterhead { left: 689px; top: 72px; width: 449px; height: 602px; }
  .letterhead .brand { position: absolute; left: 56px; top: 40px; font-size: 15px; }
  .letterhead .contact { position: absolute; left: 266px; top: 44px; white-space: nowrap; }
</style>
</head>
<body>

  <section class="sheet card-front" aria-label="Business card front">
    <p class="person">Suresh Kodandaraman<span>CEO</span></p>
    <address class="contact small-text">
      No. 17, 60 ft Road,<br>Fourth block, Hesaralu<br>Bengalooru 560071<br>Karnataka, INDIA<br>suresh.kodand@<br>fernvaledental.example
    </address>
    <svg class="band" width="178" height="8" viewBox="0 0 178 8" aria-hidden="true">
      <rect x="0" y="2" width="150" height="6" fill="var(--plum)"/>
      <polygon points="146,8 152,2 178,2 178,8" fill="var(--silver)"/>
    </svg>
  </section>

  <section class="sheet card-back" aria-label="Business card back">
    <div class="brand"><span class="brand-dot" style="width:6px;height:6px"></span>Fernvale Dental</div>
  </section>

  <section class="sheet card-plum" aria-label="Business card back, plum">
    <div class="brand brand-on-plum"><span class="brand-dot" style="width:6px;height:6px"></span>Fernvale Dental</div>
  </section>

  <section class="sheet envelope-back" aria-label="Envelope back">
    <svg class="flap" width="456" height="130" viewBox="0 0 456 130" aria-hidden="true">
      <path d="M0 0 H456 V28 Q340 60 236 118 Q228 124 220 118 Q116 60 0 28 Z" fill="var(--plum)"/>
      <path d="M0 28 Q116 60 220 118 Q228 124 236 118 Q340 60 456 28" fill="none" stroke="var(--plum-soft)" stroke-width="2"/>
    </svg>
    <div class="brand brand-on-plum"><span class="brand-dot" style="width:7px;height:7px"></span>Fernvale Dental</div>
    <address class="return small-text">No. 17, 60 ft Road, Fourth block, Hesaralu<br>Bengalooru 560071, Karnataka, INDIA</address>
  </section>

  <section class="sheet envelope-front" aria-label="Envelope front">
    <div class="brand"><span class="brand-dot" style="width:8px;height:8px"></span>Fernvale Dental</div>
    <address class="return small-text">No. 17, 60 ft Road, Fourth block, Hesaralu<br>Bengalooru 560071, Karnataka, INDIA</address>
    <svg class="band" width="456" height="10" viewBox="0 0 456 10" aria-hidden="true">
      <rect x="0" y="2" width="380" height="8" fill="var(--plum)"/>
      <polygon points="374,10 382,2 456,2 456,10" fill="var(--silver)"/>
    </svg>
  </section>

  <section class="sheet letterhead" aria-label="Letterhead">
    <div class="brand"><span class="brand-dot" style="width:9px;height:9px"></span>Fernvale Dental</div>
    <address class="contact small-text">
      No. 17, 60 ft Road,<br>Fourth block, Hesaralu<br>Bengalooru 560071<br>Karnataka, INDIA<br>suresh.kodand@fernvaledental.example
    </address>
    <svg class="band" width="449" height="12" viewBox="0 0 449 12" aria-hidden="true">
      <rect x="0" y="2" width="360" height="10" fill="var(--plum)"/>
      <polygon points="352,12 362,2 449,2 449,12" fill="var(--silver)"/>
    </svg>
  </section>

</body>
</html>
```